Weddings by Marla

Nice ad or card design to advertise my hair business. I like to accentuate 'Marla'

some of the things on my card/ad now are:

Full service hair artist
Available for your special occasion

up-do's for you or your sheitle
Temporary hair extensions, cuts, color, Hi-lites, perms, and waxing

phone, emial, website
Updates

Project Deadline Extended
Reason: I chose a design but it needed a minor change but i have not heard back from the designer. I am still hoping to finalize that design. thank you

Target Market(s)

women all ages

Industry/Entity Type

Hair

```html
<!DOCTYPE html>
<html lang="en">
<head>
<meta charset="utf-8">
<title>Marla – hair artist</title>
<link href="https://fonts.googleapis.com/css2?family=Pinyon+Script&family=Fondamento&family=Oranienbaum&family=Comfortaa:wght@300&family=Italianno&display=swap" rel="stylesheet">
<style>
  :root {
    --bg-top: #cfd0d2;
    --bg-bottom: #bdbfc1;
    --panel: #d8d9da;
    --ink: #1d1d1d;
    --frame: #4a4a4a;
    --photo-light: #e4e4e4;
    --photo-mid: #b9b9b9;
    --photo-dark: #8e8e8e;
  }
  html, body {
    margin: 0;
    padding: 0;
    overflow: hidden;
    background: #ffffff;
  }
  .card {
    position: relative;
    width: 1200px;
    height: 684px;
    box-sizing: border-box;
    border: 2px solid var(--frame);
    background: linear-gradient(180deg, var(--bg-top), var(--bg-bottom));
    overflow: hidden;
    color: var(--ink);
  }
  .portrait {
    position: absolute;
    left: 0;
    top: 34px;
    width: 395px;
    height: 650px;
    background:
      radial-gradient(ellipse 45% 40% at 40% 30%, var(--photo-mid), transparent 70%),
      radial-gradient(ellipse 70% 45% at 45% 80%, var(--photo-light), transparent 75%),
      linear-gradient(180deg, var(--photo-dark) 0%, var(--photo-mid) 45%, var(--photo-light) 100%);
    border-radius: 40% 45% 0 0 / 20% 22% 0 0;
    opacity: 0.85;
  }
  .brand-name {
    position: absolute;
    left: 512px;
    top: 20px;
    margin: 0;
    font-family: "Pinyon Script", cursive;
    font-weight: 400;
    font-size: 172px;
    line-height: 1;
    letter-spacing: 2px;
  }
  .brand-tagline {
    position: absolute;
    left: 664px;
    top: 236px;
    margin: 0;
    font-family: "Fondamento", cursive;
    font-size: 44px;
    line-height: 1;
  }
  .services {
    position: absolute;
    left: 479px;
    top: 298px;
    width: 721px;
    height: 263px;
    background: var(--panel);
    margin: 0;
    padding: 27px 0 0 58px;
    box-sizing: border-box;
    list-style: none;
    font-family: "Oranienbaum", serif;
    font-size: 30px;
    letter-spacing: 0.5px;
  }
  .services li {
    height: 60px;
    line-height: 40px;
  }
  .services li::before {
    content: "- ";
  }
  .contact {
    position: absolute;
    left: 36px;
    top: 596px;
    height: 50px;
    display: flex;
    align-items: center;
    white-space: nowrap;
  }
  .contact-icon {
    width: 40px;
    height: 40px;
    flex: none;
  }
  .contact-phone {
    font-family: "Comfortaa", sans-serif;
    font-weight: 300;
    font-size: 40px;
    margin: 0 20px 0 12px;
  }
  .contact-email {
    font-family: "Italianno", cursive;
    font-size: 44px;
    margin: 0 18px 0 14px;
  }
  .contact-social {
    font-family: "Italianno", cursive;
    font-size: 44px;
    margin-left: 12px;
  }
  .social-dot {
    width: 16px;
    height: 16px;
    border-radius: 50%;
    background: var(--ink);
    flex: none;
  }
</style>
</head>
<body>
  <div class="card">
    <div class="portrait" role="img" aria-label="Black and white photo of a bride seen from behind with a long curled updo"></div>

    <h1 class="brand-name">Marla</h1>
    <p class="brand-tagline">hair artist</p>

    <ul class="services">
      <li>Available for your special occasion.</li>
      <li>Up-do's for you or your sheitle.</li>
      <li>Temporary hair extensions.</li>
      <li>Cuts, color, Hi-lites, perms, and waxing.</li>
    </ul>

    <div class="contact">
      <svg class="contact-icon" viewBox="0 0 40 40" aria-hidden="true">
        <circle cx="20" cy="20" r="17" fill="none" stroke="#1d1d1d" stroke-width="2"/>
        <path d="M14 10 q-4 2 -2 9 q3 8 10 11 q4 1 5 -2 l-4 -4 l-3 2 q-4 -2 -6 -7 l3 -2 z" fill="#1d1d1d"/>
      </svg>
      <span class="contact-phone">410.555.0172</span>
      <svg class="contact-icon" viewBox="0 0 40 40" aria-hidden="true">
        <rect x="1" y="8" width="38" height="26" fill="#1d1d1d"/>
        <path d="M3 10 L20 24 L37 10" fill="none" stroke="#c8c9cb" stroke-width="2"/>
      </svg>
      <span class="contact-email">marlastix@mailbox.net</span>
      <span class="social-dot"></span>
      <span class="contact-social">hairbook.net/marlastix</span>
    </div>
  </div>
</body>
</html>
```